New solo practice law firm is looking for an elegant, professional, and interactive web design

I need a web design and developer for a new small law firm in Sacramento, California called Dorian Kessly Law, A Professional Corporation. I am a trial lawyer who represents average people facing difficult litigation disputes, including criminal defense as a former prosecutor and civil litigation as a civil litigator. Criminal defense includes domestic violence, battery, assault, drug possession, theft, DUI, etc. Civil litigation includes business disputes, property disputes, employment disputes, family law disputes, and immigration issues. I would like to see web designs that incorporate my logo and use the logo's navy blue and gold colors. I have uploaded the files of my logo to this brief. Please only use the navy blue and gold version. Overall, I want the design to look firm, professional, and elegant.

I plan on having the following pages on my website: (1) Home, (2) Dorian Kessly, (3) Practice Areas, (4) Insights, (5) Contact. I've hand drawn a preliminary sketch concept of what I envision the home page's layout to look like (attached with a text version). I would like your design to keep a similar layout for the homepage and incorporate my logo's colors within it but I am open to creative layout alternatives/ideas. I would like the other pages to have a similar look and feel as the home page. Some of the areas currently in my sketch do not have the full text. You can insert other text for now and I will provide the winner the full text.

In terms of the pictures on the website, I enjoy images of courthouses, columns (example attached but I cannot use this one), and, if possible, images from Sacramento, CA in my background (headshot attached). A plus would be live images that move and also sections of the webpage moving in the viewers view as they scroll down on the page. Also, it would be great to have my logo act as the tab for the website. I can provide other versions of the logo if needed.

I look forward to seeing your Wordpress designs!

People needing legal representation.

Law

Coded - Design and coding required

5+ page

Serif

• Incorporate my logo and my logo's colors.
• Live pictures and images appearing as viewers scroll on page.

```html
<!DOCTYPE html>
<html lang="en">
<head>
<meta charset="utf-8">
<title>Dorian Kessly Law</title>
<link href="https://fonts.googleapis.com/css2?family=Montserrat:wght@400;500;600;700&family=Poppins:wght@300;400;500&display=swap" rel="stylesheet">
<style>
:root{
  --navy:#13203a;
  --navy-deep:#0f1a30;
  --gold:#ab9463;
  --gold-dark:#8f7a4c;
  --white:#ffffff;
  --ink:#1d2840;
  --muted:#6d6d6d;
  --line:rgba(255,255,255,.14);
}
*{margin:0;padding:0;box-sizing:border-box}
html,body{width:1200px;height:2760px;overflow:hidden}
body{position:relative;background:var(--white);font-family:"Poppins",sans-serif;color:var(--ink)}
.abs{position:absolute}
.head{font-family:"Montserrat",sans-serif;font-weight:600;letter-spacing:.5px;line-height:1.2}
.gold{color:var(--gold)}

/* header */
.topbar{left:0;top:0;width:1200px;height:116px;background:var(--navy)}
.brand{left:60px;top:22px;display:flex;align-items:center;gap:10px}
.brand-mark{width:22px;height:22px;border:2px solid var(--gold)}
.brand-name{font-family:"Montserrat",sans-serif;font-weight:500;font-size:13px;color:var(--gold);line-height:1.3;letter-spacing:1px}
.icon-box{width:38px;height:38px;border:1px solid var(--gold);display:flex;align-items:center;justify-content:center}
.top-text{color:var(--white);font-size:12px;line-height:20px}
.consult-label{font-size:12px;color:var(--gold)}
.consult-phone{font-family:"Montserrat",sans-serif;font-weight:600;font-size:20px;color:var(--white)}
.lang{left:1050px;top:27px;width:90px;height:34px;border:1px solid rgba(255,255,255,.4);color:var(--white);font-size:12px;display:flex;align-items:center;justify-content:space-between;padding:0 12px 0 14px}

.nav{left:60px;top:94px;width:1080px;height:45px;background:var(--gold);z-index:3}
.nav-item{top:0;height:45px;display:flex;align-items:center;justify-content:center;color:var(--white);font-size:12px;transform:translateX(-50%)}
.nav-item.active{background:var(--gold-dark);padding:0 20px;height:37px;top:4px}
.nav-sep{top:14px;width:1px;height:17px;background:rgba(255,255,255,.3)}

/* hero */
.hero{left:0;top:116px;width:1200px;height:596px;background:linear-gradient(100deg,#2b2a27 0%,#57554f 30%,#3a3935 52%,#c27a3c 68%,#d9a35a 80%,#2f3a2b 100%)}
.hero-shade{left:0;top:116px;width:700px;height:596px;background:linear-gradient(90deg,rgba(0,0,0,.45),rgba(0,0,0,0))}
.hero-title{left:62px;top:274px;font-family:"Montserrat",sans-serif;font-weight:600;font-size:50px;line-height:56px;color:var(--white)}
.hero-title .hl{color:var(--gold);background:rgba(19,32,58,.85);padding:0 6px 0 2px;margin-left:-2px}
.hero-sub{left:60px;top:452px;width:440px;color:var(--white);font-size:14px;line-height:23px}
.btn{background:var(--gold);color:var(--white);font-family:"Montserrat",sans-serif;font-weight:600;font-size:15px;display:flex;align-items:center;justify-content:center;letter-spacing:.3px}
.dot{left:1128px;width:11px;height:11px;border-radius:50%;background:var(--white)}
.dot.active{background:transparent;border:2px solid var(--white);border-radius:0}

/* practice */
.practice{left:0;top:712px;width:1200px;height:540px;background:var(--navy)}
.section-title{font-size:30px;text-align:center;width:1200px;left:0}
.practice-text{left:350px;top:874px;width:500px;text-align:center;color:var(--white);font-size:12px;line-height:21px;font-weight:300}
.area{top:982px;width:210px;height:195px;border:1px solid var(--line);display:flex;flex-direction:column;align-items:center;justify-content:flex-end;padding-bottom:46px}
.area svg{margin-bottom:26px}
.area-name{font-family:"Montserrat",sans-serif;font-weight:600;font-size:15px;color:var(--white)}

/* about */
.about{left:0;top:1252px;width:1200px;height:642px;background:linear-gradient(90deg,#f7f7f7 0%,#ececec 45%,#e4e4e4 70%,#eeeeee 100%)}
.about-title{left:139px;top:1404px;font-size:30px;color:var(--ink)}
.about-text{left:137px;width:440px;font-size:12px;line-height:19.5px;color:var(--muted)}
.portrait-ring{left:648px;top:1366px;width:430px;height:430px;border-radius:50%;border:1px solid var(--gold)}
.portrait{left:657px;top:1376px;width:412px;height:412px;border-radius:50%;background:radial-gradient(circle at 50% 60%,#2a2f3a 0 34%,var(--gold) 35%)}

/* form */
.field{left:137px;width:469px;height:42px;border:1px solid #cfcfcf;border-left:3px solid var(--gold);font-size:12px;color:#555;padding:0 0 0 14px;display:flex;align-items:center}
.field.area-field{align-items:flex-start;padding-top:14px;height:90px}
.consult-title{left:702px;top:1988px;font-size:30px;color:var(--ink)}
.consult-text{left:703px;top:2075px;width:310px;font-size:12px;line-height:20px;color:var(--muted)}
.phone-frame{left:729px;top:2129px;width:250px;height:67px;border:1px solid var(--gold)}
.phone-icon{left:705px;top:2140px;width:45px;height:45px;background:var(--gold);display:flex;align-items:center;justify-content:center}
.phone-big{left:763px;top:2145px;font-family:"Montserrat",sans-serif;font-weight:600;font-size:27px;color:var(--ink)}

/* footer */
.footer{left:0;top:2346px;width:1200px;height:414px;background:var(--navy)}
.footer-bar{left:0;top:2343px;width:600px;height:4px;background:var(--gold)}
.foot-brand{left:129px;top:2470px;width:200px;text-align:center}
.foot-brand .brand-mark{margin:0 auto 14px;width:40px;height:40px}
.foot-heading{font-family:"Montserrat",sans-serif;font-weight:600;font-size:15px;color:var(--gold);letter-spacing:.5px}
.links{left:433px;top:2432px;list-style:none}
.links li{font-size:12px;color:var(--white);line-height:22.5px;display:flex;align-items:center}
.links li::before{content:"";width:5px;height:5px;background:var(--gold);margin-right:16px}
.f-icon{width:34px;height:34px;background:var(--gold);display:flex;align-items:center;justify-content:center}
.social{top:2535px;width:34px;height:34px;border:1px solid var(--gold)}
.divider{left:60px;top:2608px;width:1080px;height:1px;background:var(--line)}
.disclaimer{left:160px;top:2640px;width:880px;text-align:center;font-size:11px;line-height:20px;color:#c2c6d0;font-weight:300}
.copyright{left:0;top:2695px;width:1200px;text-align:center;font-size:11px;color:var(--white)}
</style>
</head>
<body>

<header>
  <div class="abs topbar"></div>
  <div class="abs brand"><span class="brand-mark"></span><span class="brand-name">DORIAN KESSLY LAW</span></div>

  <div class="abs icon-box" style="left:560px;top:26px">
    <svg width="16" height="20" viewBox="0 0 16 20"><path d="M8 1a6 6 0 0 0-6 6c0 4.5 6 12 6 12s6-7.5 6-12a6 6 0 0 0-6-6z" fill="none" stroke="#ab9463" stroke-width="1.6"/><circle cx="8" cy="7" r="2.2" fill="none" stroke="#ab9463" stroke-width="1.6"/></svg>
  </div>
  <div class="abs top-text" style="left:611px;top:23px">2870 Harlow Crest Ave Suite<br># 410 Elk Grove, CA 95758</div>

  <div class="abs icon-box" style="left:812px;top:26px">
    <svg width="20" height="20" viewBox="0 0 24 24"><path d="M6.6 10.8a15.2 15.2 0 0 0 6.6 6.6l2.2-2.2a1 1 0 0 1 1-.25 11.4 11.4 0 0 0 3.6.57 1 1 0 0 1 1 1V20a1 1 0 0 1-1 1A17 17 0 0 1 3 4a1 1 0 0 1 1-1h3.5a1 1 0 0 1 1 1c0 1.25.2 2.45.57 3.57a1 1 0 0 1-.25 1z" fill="none" stroke="#ab9463" stroke-width="1.6"/></svg>
  </div>
  <div class="abs consult-label" style="left:864px;top:24px">Free Consultation</div>
  <div class="abs consult-phone" style="left:862px;top:40px">(916)555-0147</div>

  <div class="abs lang">English
    <svg width="10" height="6" viewBox="0 0 10 6"><path d="M1 1l4 4 4-4" fill="none" stroke="#fff" stroke-width="1.3"/></svg>
  </div>

  <nav class="abs nav">
    <span class="abs nav-item active" style="left:206px">HOME</span>
    <span class="abs nav-item" style="left:357px">DORIAN KESSLY</span>
    <span class="abs nav-sep" style="left:453px"></span>
    <span class="abs nav-item" style="left:545px">PRACTICE AREAS</span>
    <span class="abs nav-sep" style="left:641px"></span>
    <span class="abs nav-item" style="left:710px">INSIGHTS</span>
    <span class="abs nav-sep" style="left:784px"></span>
    <span class="abs nav-item" style="left:862px">CONTACT</span>
  </nav>
</header>

<section>
  <div class="abs hero" role="img" aria-label="Courthouse columns blending into the Sacramento Tower Bridge at sunset"></div>
  <div class="abs hero-shade"></div>
  <h1 class="abs hero-title">Dorian Kessly<br><span class="hl">Professional</span><br>Corporation Law</h1>
  <p class="abs hero-sub">I Am A Trial Lawyer Who Represents Average People Facing Difficult Litigation Disputes</p>
  <div class="abs btn" style="left:60px;top:518px;width:139px;height:41px">CONTACT US</div>
  <span class="abs dot" style="top:343px"></span>
  <span class="abs dot" style="top:366px"></span>
  <span class="abs dot active" style="top:388px"></span>
  <span class="abs dot" style="top:411px"></span>
  <span class="abs dot" style="top:434px"></span>
</section>

<section>
  <div class="abs practice"></div>
  <h2 class="abs head section-title" style="top:785px;color:var(--white)">CRIMINAL AND CIVIL</h2>
  <h2 class="abs head section-title gold" style="top:822px">TRIAL LAWYERS</h2>
  <p class="abs practice-text">Dorian Kessly Law is a law firm serving the Sacramento, Yolo, San Joaquin, Solano and Stanislaus Counties. We represent clients in a wide array of criminal, civil, family law, and immigration cases.</p>

  <div class="abs area" style="left:181px">
    <svg width="70" height="70" viewBox="0 0 70 70" fill="none" stroke="#fff" stroke-width="2.5"><circle cx="20" cy="52" r="14"/><circle cx="52" cy="20" r="14"/><path d="M25 38l6-12 6-6" stroke="#ab9463"/></svg>
    <span class="area-name">Criminal Defense</span>
  </div>
  <div class="abs area" style="left:390.5px">
    <svg width="70" height="70" viewBox="0 0 70 70" fill="none" stroke-width="2.5"><path d="M35 6v60M20 66h30M10 16h50" stroke="#fff"/><path d="M14 16L4 40h20zM56 16l-10 24h20zM4 40a10 6 0 0 0 20 0M46 40a10 6 0 0 0 20 0" stroke="#ab9463"/></svg>
    <span class="area-name">Civil Litigation</span>
  </div>
  <div class="abs area" style="left:600px">
    <svg width="70" height="70" viewBox="0 0 70 70" fill="none" stroke-width="2.5"><rect x="8" y="4" width="46" height="62" stroke="#fff"/><circle cx="31" cy="36" r="13" stroke="#ab9463"/><path d="M18 36h26M31 23v26" stroke="#ab9463"/><path d="M16 12h30" stroke="#fff"/></svg>
    <span class="area-name">Immigration</span>
  </div>
  <div class="abs area" style="left:809.5px">
    <svg width="70" height="70" viewBox="0 0 70 70" fill="none" stroke-width="2.5"><path d="M8 34L35 10l27 24" stroke="#fff"/><path d="M15 28v36h40V28" stroke="#fff"/><path d="M35 56l-10-10a6 6 0 0 1 10-7 6 6 0 0 1 10 7z" stroke="#ab9463"/></svg>
    <span class="area-name">Family Law</span>
  </div>
</section>

<section>
  <div class="abs about" role="img" aria-label="Faded courthouse facade with classical columns"></div>
  <h2 class="abs head about-title">READY, RELIABLE, &amp;<br><span class="gold">EXPERIENCED</span></h2>
  <p class="abs about-text" style="top:1500px">Lorem Ipsum has been the industry's standard dummy text ever since the 1500s, when an unknown printer took a galley of type and scrambled it to make a type specimen book.</p>
  <p class="abs about-text" style="top:1570px;width:455px">Lorem Ipsum has been the industry's standard dummy text ever since the 1500s, when an unknown printer took a galley of type and scrambled it to make a type specimen book. It has survived not only five centuries, but also the leap into electronic industry typesetting, remaining essentially unchanged.</p>
  <div class="abs btn" style="left:135px;top:1670px;width:157px;height:41px">ABOUT DORIAN</div>
  <div class="abs portrait-ring"></div>
  <div class="abs portrait" role="img" aria-label="Portrait of the attorney in a dark suit on a gold circle"></div>
</section>

<section>
  <div class="abs field" style="top:1972px">Name *</div>
  <div class="abs field" style="top:2024px">Email*</div>
  <div class="abs field" style="top:2076px">Phone *</div>
  <div class="abs field area-field" style="top:2128px">Please Enter a Brief Description of Your Case ....</div>
  <div class="abs btn" style="left:138px;top:2231px;width:101px;height:41px">SUBMIT</div>

  <h2 class="abs head consult-title">SCHEDULE A FREE<br><span class="gold">CONSULTATION</span></h2>
  <p class="abs consult-text">When You Contact Dorian Kessly Law For a Free Consultation...</p>
  <div class="abs phone-frame"></div>
  <div class="abs phone-icon">
    <svg width="26" height="26" viewBox="0 0 24 24"><path d="M6.6 10.8a15.2 15.2 0 0 0 6.6 6.6l2.2-2.2a1 1 0 0 1 1-.25 11.4 11.4 0 0 0 3.6.57 1 1 0 0 1 1 1V20a1 1 0 0 1-1 1A17 17 0 0 1 3 4a1 1 0 0 1 1-1h3.5a1 1 0 0 1 1 1c0 1.25.2 2.45.57 3.57a1 1 0 0 1-.25 1z" fill="none" stroke="#fff" stroke-width="1.6"/></svg>
  </div>
  <div class="abs phone-big">(916)555-0147</div>
</section>

<footer>
  <div class="abs footer"></div>
  <div class="abs footer-bar"></div>
  <div class="abs foot-brand">
    <div class="brand-mark"></div>
    <div class="brand-name" style="font-size:15px;letter-spacing:2px">DORIAN KESSLY LAW</div>
  </div>

  <h3 class="abs foot-heading" style="left:433px;top:2394px">QUICK LINKS</h3>
  <ul class="abs links">
    <li>Home</li><li>Dorian Kessly</li><li>Practice Areas</li><li>Insights</li><li>Contact</li><li>Privacy Policy</li>
  </ul>

  <h3 class="abs foot-heading" style="left:806px;top:2394px">CONTACT INFO</h3>
  <div class="abs f-icon" style="left:803px;top:2437px">
    <svg width="14" height="18" viewBox="0 0 16 20"><path d="M8 1a6 6 0 0 0-6 6c0 4.5 6 12 6 12s6-7.5 6-12a6 6 0 0 0-6-6z" fill="none" stroke="#fff" stroke-width="1.8"/><circle cx="8" cy="7" r="2.2" fill="none" stroke="#fff" stroke-width="1.8"/></svg>
  </div>
  <div class="abs top-text" style="left:854px;top:2437px;font-size:12px">2870 Harlow Crest Ave Suite #<br>410 Elk Grove, CA 95758</div>
  <div class="abs f-icon" style="left:803px;top:2486px">
    <svg width="18" height="18" viewBox="0 0 24 24"><path d="M6.6 10.8a15.2 15.2 0 0 0 6.6 6.6l2.2-2.2a1 1 0 0 1 1-.25 11.4 11.4 0 0 0 3.6.57 1 1 0 0 1 1 1V20a1 1 0 0 1-1 1A17 17 0 0 1 3 4a1 1 0 0 1 1-1h3.5a1 1 0 0 1 1 1c0 1.25.2 2.45.57 3.57a1 1 0 0 1-.25 1z" fill="none" stroke="#fff" stroke-width="1.8"/></svg>
  </div>
  <div class="abs" style="left:855px;top:2492px;color:var(--white);font-size:17px">(916) 555-0147</div>
  <span class="abs social" style="left:803px"></span>
  <span class="abs social" style="left:843px"></span>
  <span class="abs social" style="left:882px"></span>

  <div class="abs divider"></div>
  <p class="abs disclaimer">The information on this website is for general information purposes only. Nothing on this site should be taken as legal advice for any individual case or situation. This information is not intended to create, and receipt of viewing does not constitute an attorney-client relationship</p>
  <p class="abs copyright"><span class="gold">©Dorian Kessly Law A Professional Corporation</span> - 2021 All Rights Reserved</p>
</footer>

</body>
</html>
```